A comunicação apenas pelo chat ou com desenvolvedor que não se comunica com cliente é péssimo ! O desenvolvedor que não se comunica dificulta o desenvolvimento do trabalho causando uma demora ecessiva !

```html
<!DOCTYPE html>
<html lang="pt-BR">
<head>
<meta charset="UTF-8">
<title>Traço Norte Obras — Cartão de visita</title>
<link href="https://fonts.googleapis.com/css2?family=Exo+2:wght@500;600&family=Open+Sans:wght@400;600;700&display=swap" rel="stylesheet">
<style>
  :root {
    --page: #ffffff;
    --frame: #e6e6e6;
    --card: #b8b8b8;
    --band-light: #c3c3c3;
    --band-dark: #bcbcbc;
    --ink: #111111;
    --ink-soft: #2a2a2a;
  }
  * { box-sizing: border-box; margin: 0; padding: 0; }
  html, body { width: 1200px; height: 1200px; overflow: hidden; }
  body {
    background: var(--page);
    border: 6px solid var(--frame);
    position: relative;
    font-family: "Open Sans", Arial, sans-serif;
    color: var(--ink);
  }
  .card {
    position: absolute;
    left: 203px;
    width: 782px;
    background: var(--card);
    overflow: hidden;
  }
  .card-front { top: 85px; height: 450px; }
  .card-back { top: 647px; height: 462px; }

  .brand {
    position: absolute;
    inset: 0;
    display: flex;
    align-items: center;
    justify-content: center;
    gap: 26px;
  }
  .brand-square {
    width: 104px; height: 84px;
    background: var(--ink);
  }
  .brand-name {
    font-family: "Exo 2", Arial, sans-serif;
    font-weight: 500;
    font-size: 38px;
    line-height: 1.12;
    letter-spacing: 3px;
    color: var(--ink);
    text-transform: uppercase;
  }

  .texture {
    position: absolute;
    left: 0; right: 0; top: 160px; bottom: 0;
    background: linear-gradient(180deg, var(--band-light) 0%, var(--band-dark) 100%);
  }

  .back-brand {
    position: absolute;
    left: 92px; top: 196px;
    font-family: "Exo 2", Arial, sans-serif;
    font-weight: 600;
    font-size: 40px;
    line-height: 1.05;
    letter-spacing: 2px;
    color: var(--ink);
    text-transform: uppercase;
  }

  .holder {
    position: absolute;
    right: 48px; top: 94px;
    text-align: right;
  }
  .holder-name { font-weight: 700; font-size: 30px; line-height: 1.1; }
  .holder-role { font-weight: 400; font-size: 21px; color: var(--ink-soft); }

  .contacts {
    position: absolute;
    right: 48px; top: 198px;
    list-style: none;
    text-align: right;
  }
  .contacts li {
    display: flex;
    justify-content: flex-end;
    align-items: center;
    gap: 12px;
    font-weight: 600;
    font-size: 16px;
    height: 27px;
  }
  .contacts li.gap-before { margin-top: 22px; }
  .contacts svg { width: 22px; height: 22px; flex: none; }
</style>
</head>
<body>
  <section class="card card-front">
    <div class="brand">
      <span class="brand-square"></span>
      <span class="brand-name">Traço Norte<br>Obras</span>
    </div>
  </section>

  <section class="card card-back">
    <div class="texture" role="img" aria-label="Padrão decorativo de faixas cinza claras"></div>

    <div class="back-brand">Traço<br>Norte</div>

    <div class="holder">
      <p class="holder-name">Nome Sobrenome</p>
      <p class="holder-role">cargo</p>
    </div>

    <ul class="contacts">
      <li>+55 37 8888-9999
        <svg viewBox="0 0 24 24"><circle cx="12" cy="12" r="10" fill="none" stroke="#111" stroke-width="2"/><path d="M8.5 7c.6-.4 1.2 0 1.5.6l.7 1.5c.2.5 0 1-.4 1.3l-.6.5c.6 1.3 1.7 2.4 3 3l.5-.6c.3-.4.8-.6 1.3-.4l1.5.7c.6.3 1 .9.6 1.5-.6 1-1.7 1.6-2.9 1.2C10.6 16.4 7.6 13.4 6.8 10c-.3-1.2.7-2.4 1.7-3z" fill="#111"/></svg>
      </li>
      <li>contato@contato.com.br
        <svg viewBox="0 0 24 24"><rect x="3" y="6" width="18" height="12" fill="#111"/><path d="M3.5 6.5L12 13l8.5-6.5" fill="none" stroke="#c0c0c0" stroke-width="1.6"/></svg>
      </li>
      <li>www.site.com.br
        <svg viewBox="0 0 24 24"><g fill="none" stroke="#111" stroke-width="1.8"><circle cx="12" cy="12" r="9"/><ellipse cx="12" cy="12" rx="4" ry="9"/><path d="M3 12h18M5 7.5h14M5 16.5h14"/></g></svg>
      </li>
      <li class="gap-before">Endereço: Exemplo - N 11
        <svg viewBox="0 0 24 24"><circle cx="12" cy="12" r="6.5" fill="none" stroke="#111" stroke-width="3"/></svg>
      </li>
      <li>social/tracoNorte
        <svg viewBox="0 0 24 24"><rect x="4" y="4" width="16" height="16" rx="2" fill="#111"/></svg>
      </li>
    </ul>
  </section>
</body>
</html>
```